Business card for Eyelash extension salon in Beverly Hills,California USA

We need new business card for our salon in Beverly Hills. The salon name is 'Lumarra' . We would like to have...Business name: Lumarra Name of person: will provide later Address 6128 N.Corbel Ridge Blvd Beverly Hills , CA 90210 Phone: will provide later (Text only) Web: www.lumarrastudio-example.com Pictogrid icon, Friendvale icon follow us for seasonal campaign and news @lumarrastudioexample Design should look elegant, high-end, clean, simple, cohesive with my brand. Please refer my brand board. Business name color will be metallic bronzy color. Im thinking grey background or white background. Thanks

Target Market(s)

25-35. Gender neutral. People who are in Entertainment business industry.
This is High-end Eyelash extension salon in Beverly Hills

Industry/Entity Type

Beauty Salon

Contact Information for Business Card

Business name: Lumarra
Name of person: will provide later
Address 6128 N.Corbel Ridge Blvd Beverly Hills , CA 90210
Phone: will provide later (Text only)
Web: www.lumarrastudio-example.com
Pictogrid icon, Friendvale icon
follow us for seasonal campaign and news @lumarrastudioexample

Requirements
Must have
• Beautiful, elegant, clean and simple look but very attractive and modern
Should not have
• We don't like too clutter, too busy designs.

```html
<!DOCTYPE html>
<html lang="en">
<head>
<meta charset="utf-8">
<title>Lumarra – Business Card Options</title>
<link rel="stylesheet" href="https://fonts.googleapis.com/css2?family=Open+Sans:wght@400&display=swap">
<style>
  :root {
    --bronze: #8b6239;
    --logo-brown: #8b6a4e;
    --rose: #ea1659;
    --silver: #b5b5b5;
    --ink: #111111;
    --paper: #ffffff;
  }
  html, body {
    margin: 0;
    width: 1200px;
    height: 1200px;
    overflow: hidden;
    background: var(--paper);
    font-family: "Open Sans", sans-serif;
  }
  .canvas {
    position: relative;
    width: 1200px;
    height: 1200px;
  }
  .card {
    position: absolute;
    box-sizing: border-box;
    border: 2px solid var(--ink);
    border-bottom-width: 6px;
    overflow: hidden;
  }
  .card svg { display: block; width: 100%; height: 100%; }
  .card--bronze { left: 118px; top: 13px; width: 964px; height: 580px; background: var(--bronze); }
  .card--silver { left: 114px; top: 608px; width: 966px; height: 582px; background: var(--silver); }
  .brand-name {
    font-family: "Open Sans", sans-serif;
    font-weight: 400;
    fill: var(--logo-brown);
    letter-spacing: 2px;
  }
  .address { font-family: "Open Sans", sans-serif; font-size: 24px; }
  .website { font-family: "Open Sans", sans-serif; font-size: 38px; }
  .text-dark { fill: var(--ink); }
  .text-rose { fill: var(--rose); }
</style>
</head>
<body>
<main class="canvas">

  <section class="card card--bronze" aria-label="Business card, bronze version">
    <svg viewBox="0 0 1204 720" preserveAspectRatio="none">
      <ellipse class="oval-rim" cx="650" cy="402" rx="700" ry="372" fill="var(--rose)"/>
      <ellipse class="oval-face" cx="662" cy="410" rx="688" ry="360" fill="var(--paper)"/>
      <text class="brand-name" x="436" y="385" text-anchor="middle" font-size="150">Lumarra</text>
      <rect class="divider" x="349" y="582" width="499" height="9" fill="var(--rose)"/>
      <text class="address text-dark" x="599" y="633" text-anchor="middle">N.Corbel Ridge Blvd Larkmont Vale, CA 90877</text>
      <text class="website text-dark" x="599" y="676" text-anchor="middle">www.lumarrastudio-example.com</text>
    </svg>
  </section>

  <section class="card card--silver" aria-label="Business card, silver version">
    <svg viewBox="0 0 1207 720" preserveAspectRatio="none">
      <defs>
        <clipPath id="upper-rim">
          <polygon points="0,0 1207,0 1207,240 0,330"/>
        </clipPath>
      </defs>
      <ellipse class="oval-rim" cx="652" cy="402" rx="702" ry="372" fill="var(--rose)"/>
      <ellipse class="oval-rim-dark" cx="652" cy="402" rx="702" ry="372" fill="var(--ink)" clip-path="url(#upper-rim)"/>
      <ellipse class="oval-face" cx="664" cy="410" rx="690" ry="360" fill="var(--paper)"/>
      <text class="brand-name" x="438" y="385" text-anchor="middle" font-size="150">Lumarra</text>
      <rect class="divider" x="350" y="582" width="500" height="9" fill="var(--rose)"/>
      <text class="address text-rose" x="600" y="633" text-anchor="middle">N.Corbel Ridge Blvd Larkmont Vale, CA 90877</text>
      <text class="website text-rose" x="600" y="676" text-anchor="middle">www.lumarrastudio-example.com</text>
    </svg>
  </section>

</main>
</body>
</html>
```